Birchfield Dental Care Stationery

create stationery, business cards and envelops for business. Use current logo on website but open to new fonts for the business name. Business name is Birchfield Dental Care, would like below the name added "Cosmetic - Family - Implants" Website is www.birchfielddentalcareQX.example. I would like to have modern look, clean, and professional. The water mark of the logo is a great thing to ad as well.

Target Market(s)

General public, Families, Cosmetic, Implant

Industry/Entity Type

Dental

Font styles to use
Sans Serif

Colors
9bcb3c
000000
757575
c9c9c9

Requirements
Must have
• Would like to see different versions of the current logo. Improvements, color, sytle, and class.
Nice to have
• current font has double "oo" in the Birchfield logo, does not need to have with new logo.

```html
<!DOCTYPE html>
<html lang="en">
<head>
<meta charset="utf-8">
<title>Birchfield Dental Care – Business Card</title>
<link href="https://fonts.googleapis.com/css2?family=Lato:wght@400;700;900&display=swap" rel="stylesheet">
<style>
  :root {
    --page-bg: #e4e5e7;
    --card-top: #4a5566;
    --card-bottom: #2f3744;
    --card-edge: #262c36;
    --accent-green: #9bcb3c;
    --text-white: #ffffff;
    --text-soft: #dfe3e8;
  }
  * { margin: 0; padding: 0; box-sizing: border-box; }
  html, body {
    width: 1200px; height: 780px; overflow: hidden;
    background: var(--page-bg);
    font-family: "Lato", Arial, sans-serif;
  }
  .canvas {
    position: relative; width: 1200px; height: 780px;
    display: flex; align-items: center; justify-content: center; gap: 40px;
  }
  .card {
    position: relative; width: 540px; height: 310px;
    border-radius: 18px; overflow: hidden;
    background: radial-gradient(ellipse at 60% 25%, var(--card-top), var(--card-bottom) 75%);
    box-shadow: 0 2px 0 var(--card-edge), 0 14px 30px rgba(0,0,0,.22);
    color: var(--text-white);
  }

  /* Front */
  .name-band {
    position: absolute; left: 0; top: 160px; width: 214px; height: 84px;
    background: var(--accent-green);
    padding: 18px 0 0 32px;
  }
  .person-name { font-weight: 700; font-size: 21px; letter-spacing: .5px; text-transform: uppercase; line-height: 1.1; }
  .person-role { font-size: 15px; color: #f4f9ea; margin-top: 2px; }
  .brand-mark {
    position: absolute; display: flex; align-items: center; gap: 14px;
  }
  .front .brand-mark { left: 176px; top: 62px; }
  .brand-dot {
    width: 78px; height: 78px; border-radius: 50%;
    border: 4px solid var(--accent-green); background: var(--card-bottom);
    flex: none;
  }
  .brand-name {
    font-weight: 700; font-size: 30px; line-height: 1.05; color: var(--text-white);
  }
  .contact {
    position: absolute; left: 262px; top: 166px; width: 256px;
    font-size: 13px; line-height: 1.45; color: var(--text-soft);
  }
  .contact-line { display: flex; align-items: center; gap: 7px; white-space: nowrap; }
  .contact-icon { width: 15px; height: 15px; flex: none; }
  .address { margin-bottom: 3px; }

  /* Back */
  .back-layout {
    position: absolute; inset: 0;
    display: flex; flex-direction: column; align-items: center; justify-content: center;
  }
  .back .brand-dot { width: 96px; height: 96px; margin-bottom: 18px; }
  .back .brand-name { font-size: 36px; text-align: center; }
  .tagline { margin-top: 10px; font-size: 17px; color: var(--accent-green); letter-spacing: .4px; }
</style>
</head>
<body>
<main class="canvas">

  <section class="card front" aria-label="Business card front">
    <div class="brand-mark">
      <span class="brand-dot"></span>
      <span class="brand-name">Birchfield<br>Dental Care</span>
    </div>

    <div class="name-band">
      <p class="person-name">Dana Keller</p>
      <p class="person-role">Manager</p>
    </div>

    <div class="contact">
      <p class="address">1280 N Alder Ln Westbrook City<br>QX 40512-1100</p>
      <p class="contact-line">
        <svg class="contact-icon" viewBox="0 0 16 16" aria-hidden="true"><rect width="16" height="16" rx="3" fill="#9bcb3c"/><path d="M5 3.5l2 2-1 1.3c.6 1.3 1.6 2.3 2.9 2.9l1.3-1 2 2-1.2 1.3C8 11.8 4.2 8 4 4.7z" fill="#2f3744"/></svg>
        555-014-2290
      </p>
      <p class="contact-line">
        <svg class="contact-icon" viewBox="0 0 16 16" aria-hidden="true"><rect width="16" height="16" rx="3" fill="#9bcb3c"/><path d="M5 3.5l2 2-1 1.3c.6 1.3 1.6 2.3 2.9 2.9l1.3-1 2 2-1.2 1.3C8 11.8 4.2 8 4 4.7z" fill="#2f3744"/></svg>
        (555) 014-2291
      </p>
      <p class="contact-line">
        <svg class="contact-icon" viewBox="0 0 16 16" aria-hidden="true"><rect width="16" height="16" rx="3" fill="#9bcb3c"/><g fill="none" stroke="#2f3744" stroke-width="1.1"><circle cx="8" cy="8" r="4.5"/><ellipse cx="8" cy="8" rx="2" ry="4.5"/><path d="M3.5 8h9"/></g></svg>
        www.birchfielddentalcareQX.example
      </p>
    </div>
  </section>

  <section class="card back" aria-label="Business card back">
    <div class="back-layout">
      <span class="brand-dot"></span>
      <p class="brand-name">Birchfield Dental Care</p>
      <p class="tagline">Cosmetic - Family - Implants</p>
    </div>
  </section>

</main>
</body>
</html>
```